Business Card Design

We are looking for a business card designed for our landscaping company. We do landscaping installation & Maintenance Services. We would like to see designs that have basic landscaping in background. We also think it is important to have both of our names and phone numbers on the card. We need something that stands out a little whether it is shape of the card or thickness or design.

Industry/Entity Type

Business

Contact Information for Business Card

Pale Ridge Yardworks, paleridgeyardworks@mailbrook.net, Dale Purvine 555-213-7690, Martin Kolbey 555-864-1037

```html
<!DOCTYPE html>
<html lang="en">
<head>
<meta charset="utf-8">
<title>Pale Ridge Yardworks – Business Card</title>
<link href="https://fonts.googleapis.com/css2?family=Arimo:wght@400;700&display=swap" rel="stylesheet">
<style>
  :root {
    --backdrop: #dfe3e8;
    --card-white: #ffffff;
    --leaf-dark: #2f6a22;
    --leaf-mid: #5f9a3a;
    --leaf-light: #a7c93f;
    --band-green: #7f9d35;
    --name-green: #2c5a25;
    --garden-deep: #24461c;
    --garden-mid: #4f8232;
    --garden-bright: #86b04a;
  }
  html, body {
    margin: 0;
    width: 1200px;
    height: 900px;
    overflow: hidden;
    background: var(--backdrop);
    font-family: "Arimo", Arial, sans-serif;
  }
  .card {
    position: absolute;
    left: 75px;
    top: 150px;
    width: 1050px;
    height: 600px;
    background: var(--card-white);
    box-shadow: 0 10px 30px rgba(0,0,0,0.18);
    overflow: hidden;
  }
  .card-shapes {
    position: absolute;
    inset: 0;
  }
  .brand {
    position: absolute;
    left: 150px;
    top: 120px;
    width: 760px;
    text-align: center;
    transform: rotate(-2.2deg);
  }
  .brand-name {
    margin: 0;
    font-size: 64px;
    font-weight: 700;
    color: var(--leaf-light);
    letter-spacing: 1px;
  }
  .brand-tagline {
    margin: 6px 0 0;
    font-size: 25px;
    font-weight: 400;
    color: var(--card-white);
  }
  .contacts {
    position: absolute;
    left: 420px;
    top: 320px;
    display: flex;
    transform: rotate(-2.2deg);
  }
  .contact {
    padding: 0 22px;
    color: var(--name-green);
  }
  .contact-left { text-align: right; border-right: 3px solid var(--leaf-mid); }
  .contact-name {
    margin: 0;
    font-size: 38px;
    font-weight: 700;
  }
  .contact-phone {
    margin: 6px 0 0;
    font-size: 34px;
    display: flex;
    align-items: center;
    gap: 8px;
  }
  .contact-left .contact-phone { justify-content: flex-end; }
  .phone-icon { width: 28px; height: 28px; fill: var(--leaf-mid); }
  .email {
    position: absolute;
    right: 40px;
    top: 476px;
    margin: 0;
    font-size: 30px;
    color: var(--card-white);
    transform: rotate(-2.2deg);
  }
</style>
</head>
<body>
  <article class="card">
    <svg class="card-shapes" width="1050" height="600" viewBox="0 0 1050 600">
      <defs>
        <linearGradient id="garden-tones" x1="0" y1="0" x2="1" y2="1">
          <stop offset="0" stop-color="var(--garden-mid)"/>
          <stop offset="0.5" stop-color="var(--garden-deep)"/>
          <stop offset="1" stop-color="var(--garden-bright)"/>
        </linearGradient>
      </defs>
      <polygon class="garden-photo" role="img" aria-label="Photo of a lush landscaped garden with trimmed shrubs and flower beds"
               points="0,0 1050,0 1050,262 0,302" fill="url(#garden-tones)"/>
      <line class="photo-edge" x1="0" y1="300" x2="1050" y2="260" stroke="var(--card-white)" stroke-width="3" stroke-dasharray="14 6"/>
      <polygon class="accent-band" points="0,510 1050,470 1050,520 0,560" fill="var(--band-green)"/>
      <polygon class="garden-strip" role="img" aria-label="Photo strip of garden hedges and a stone path"
               points="0,560 1050,520 1050,600 0,600" fill="url(#garden-tones)"/>
    </svg>

    <header class="brand">
      <h1 class="brand-name">Pale Ridge Yardworks</h1>
      <p class="brand-tagline">landscaping installation &amp; Maintenance Services</p>
    </header>

    <section class="contacts">
      <div class="contact contact-left">
        <p class="contact-name">Dale Purvine</p>
        <p class="contact-phone">555-213-7690
          <svg class="phone-icon" viewBox="0 0 24 24"><path d="M3 9c0-3 4-5 9-5s9 2 9 5l-1 2-4-1v-2c-2-1-6-1-8 0v2l-4 1zM6 13l3-3h6l3 3v6H6z"/></svg>
        </p>
      </div>
      <div class="contact contact-right">
        <p class="contact-name">Martin Kolbey</p>
        <p class="contact-phone">
          <svg class="phone-icon" viewBox="0 0 24 24"><path d="M3 9c0-3 4-5 9-5s9 2 9 5l-1 2-4-1v-2c-2-1-6-1-8 0v2l-4 1zM6 13l3-3h6l3 3v6H6z"/></svg>
          555-864-1037</p>
      </div>
    </section>

    <p class="email">paleridgeyardworks@mailbrook.net</p>
  </article>
</body>
</html>
```